ATTORNEY FULL PAGE AD

We need a full page flyer for our law firm. We are sending it to people who were in an auto accident and injured. I want to let people know that by hiring an attorney that does not mean that they are suing someone. We will just help them in filing a claim and to get them compensated for: medical bills, lost wages, car repairs, future medical treatment or surgery, and pain/suffering. They will NOT have to pay us any money unless we get them paid. I want to show that we are compassionate to the fact that they went through this tramatic event that will effect their lives for ever. They do not have to worry about anything once they hire us. Our website is: www.brightwelllawfirm.com Our colors are black and gold. NO GAMBLING REFERENCES!!!!
Updates

Don't worry so much about content and wording. Once we get a design and images that look great we will message you the exact words we would like put into the paragraphs. The overall "look" and images are the most important. If anyone has a great change-up logo we are open to it as well. Thanks for everyone's hard work!

We like the dark colors. Some of the images are a little cheesy. We are a family business and treat are clients as family. I like the pictures o the car crashes an the hands. No blood. We want to come off as respectful and trustworthy. It's more about how we will care for them as family than getting them lots of money. 

Target Market(s)

People who were in major accidents and have serious injuries

Industry/Entity Type

Attorney

Requirements
Must have
• Must have our phone number: 1-855-MBRIGHT
Website: www.brightwelllawfirm.com
Company name: Brightwell Law Group
Attorney name: Morgan Ellis Brightwell
High gloss with card stock paper.
Classy - NOT cheesy
Should not have
• No cartoons. Very masculine and professional. There may have been death involved in the accident so we want the ad to be very compassionate and moving.

```html
<!DOCTYPE html>
<html lang="en">
<head>
<meta charset="utf-8">
<title>Brightwell Law Group – Personal Injury Flyer</title>
<link href="https://fonts.googleapis.com/css2?family=Jost:wght@400;500;700&family=Cinzel:wght@400&display=swap" rel="stylesheet">
<style>
  :root {
    --page-bg: #e9e6e1;
    --sheet-bg: #dcdcdc;
    --ink: #2b2b2b;
    --ink-soft: #3a3a3a;
    --label-bg: #5a5a5a;
    --label-ink: #ffffff;
    --footer-bg: #575757;
    --footer-rule: #9a9a9a;
    --wave-dark: #8c8c8c;
    --divider: #a8a8a8;
    --brand-gold: #c9a62a;
    --sepia-light: #c9ad7c;
    --sepia-mid: #8e6f43;
    --sepia-dark: #3b2a16;
    --icon: #7d7d7d;
  }
  * { margin: 0; padding: 0; box-sizing: border-box; }
  html, body { width: 950px; height: 1200px; overflow: hidden; }
  body { background: var(--page-bg); font-family: "Jost", sans-serif; color: var(--ink); position: relative; }

  .flyer { position: absolute; left: 50px; top: 50px; width: 850px; height: 1100px; background: var(--sheet-bg); overflow: hidden; }

  .hero-photo { position: absolute; left: 0; top: 0; width: 850px; height: 350px;
    background: linear-gradient(100deg, var(--sepia-light) 0%, var(--sepia-mid) 45%, var(--sepia-dark) 70%, var(--sepia-mid) 100%); }
  .hero-wave { position: absolute; left: 0; top: 230px; width: 850px; height: 140px; }

  .column-divider { position: absolute; left: 497px; top: 360px; width: 1px; height: 685px; background: var(--divider); }

  .brand { position: absolute; left: 72px; top: 383px; width: 353px; height: 145px; display: flex; align-items: center; justify-content: center; }
  .brand-name { font-family: "Jost", sans-serif; font-weight: 500; font-size: 31px; color: var(--brand-gold); letter-spacing: 1px; text-transform: uppercase; text-align: center; line-height: 1.2; }
  .attorney-name { position: absolute; left: 72px; width: 353px; top: 542px; text-align: center; font-family: "Cinzel", serif; font-size: 15px; color: var(--ink-soft); letter-spacing: 0.5px; }

  .about { position: absolute; left: 18px; top: 598px; width: 467px; }
  .about h2 { font-weight: 400; font-size: 18.5px; letter-spacing: 0.3px; text-transform: uppercase; margin-bottom: 14px; }
  .about p { font-size: 17px; line-height: 21.8px; letter-spacing: 0.35px; text-align: justify; margin-bottom: 20px; }

  .services { position: absolute; left: 508px; top: 390px; width: 330px; }
  .services h2 { text-align: center; font-weight: 700; font-size: 23px; letter-spacing: 0.5px; margin-bottom: 20px; color: var(--ink-soft); }
  .service { font-size: 13px; line-height: 16.3px; letter-spacing: 0.2px; text-align: justify; margin-bottom: 13px; }
  .service-label { background: var(--label-bg); color: var(--label-ink); font-weight: 700; padding: 0 4px 0 10px; text-transform: uppercase; }

  .social-links { position: absolute; left: 598px; top: 1000px; display: flex; gap: 18px; }
  .social-links span { width: 36px; height: 36px; border-radius: 6px; background: var(--icon); display: block; }

  .footer { position: absolute; left: 0; top: 1045px; width: 850px; height: 46px; background: var(--footer-bg); border-top: 3px solid var(--footer-rule);
    color: #fff; font-weight: 500; font-size: 23px; display: flex; align-items: center; padding-left: 16px; }
</style>
</head>
<body>
  <main class="flyer">
    <div class="hero-photo" role="img" aria-label="Sepia-toned photo of law library shelves lined with bound legal volumes"></div>
    <svg class="hero-wave" viewBox="0 0 850 140" preserveAspectRatio="none" aria-hidden="true">
      <path d="M0,30 C200,5 430,100 850,112 V140 H0 Z" fill="var(--wave-dark)"/>
      <path d="M0,52 C220,28 440,112 850,122 V140 H0 Z" fill="var(--sheet-bg)"/>
    </svg>

    <div class="column-divider"></div>

    <div class="brand"><span class="brand-name">Brightwell Law Group</span></div>
    <p class="attorney-name">Morgan Ellis Brightwell</p>

    <section class="about">
      <h2>What is Brightwell Law Group?</h2>
      <p>The Brightwell Law Group is a personal injury law firm based in Larkmoor Bay, Easton. Our dedicated team of attorneys and staff is here to assist you with the following personal injury claims.</p>
      <p>Car accidents, big truck accidents, DUI injury accidents, motorcycle accident, pedestrian accident injury, passenger accident injury, worker's compensation, medical malpractice, nursing home abuse, dog bite injury, hospital injury, dental injury, pharmaceutical injury and premise injury, as well as several other injury claims.</p>
      <p>If you decide on Brightwell Law Group to handle your personal injury claim, you pay no money out of your pocket unless we win your case. Call the Brightwell Law Group now for a free, informational consultation to discuss your personal injury claim.</p>
    </section>

    <section class="services">
      <h2>PERSONAL INJURY</h2>
      <p class="service"><span class="service-label">Auto Accident</span> The Personal Injury aspect of the law is a complex arena. The BRIGHTWELL LAW GROUP, LLC litigates Personal Injury claims, including automobile accidents ranging from soft tissue injuries to more catastrophic accidents. Do not risk your injuries with an inexperienced attorney or try to handle a claim by yourself. Call now to receive a free, no obligation consultation.</p>
      <p class="service"><span class="service-label">DUI Accident</span> DUI accidents are a horrible thing for families and individuals to have to deal with. However, BRIGHTWELL LAW GROUP, LLC is greatly experienced in DUI cases, garnering headlines and TV news in Easton. If you are a victim of the carelessness of a DUI driver, we will work hard to get you the settlement you deserve, which may include recovery for property damage, medical bills, lost wages and suffering. Our legal representation is essential in dealing with stubborn insurance companies and getting maximum return on your claim.</p>
      <p class="service"><span class="service-label">Medical Malpractice</span> Medical professionals are not perfect, and sometimes they mess up. Unfortunately, a simple medical mistake could mean bad news for you if you happen to be on the receiving end of their error. In the case of such an event, you may be entitled to compensation. While medical malpractice can present a very tricky legal situation, The BRIGHTWELL LAW GROUP, LLC is intensely dedicated to Personal Injury claims which may involve malpractice, including Hospital Malpractice, Nursing Home Abuse, and Wrongful Death.</p>
    </section>

    <nav class="social-links" aria-label="Social media">
      <span></span><span></span><span></span>
    </nav>

    <footer class="footer">Contact Us: 1-855-MBRIGHT&nbsp;&nbsp;|&nbsp;&nbsp;Log on: www.brightwelllawfirm.com</footer>
  </main>
</body>
</html>
```